Lone Star Wetland Flora Stewardship Guild

We need to design the home page of this new website. We would like a fun website design for provides as a resource for members and information for potential members.
Please design so that we can see a portion of background on each side on the website.
I just need the final design files psd no coding needed.
Attached is their logo (colors are not 100% set in stone either so can mess with those as I did in the quick mockup attached)
Attached is a pdf newsletter they send out, you can get a feel for them and what they are about. The design is crappy and we are here to fix that going forward and we are starting with the website.
Here are some quick example websites (design style is open)
- I attached a quick mockup i did just for a content visual but by all means do what you want.
- http://www.brindlecourtleaders.org/
- http://www.qvelto.org/
- http://preview.plimworks7.com/view.php?cat=layoutpacks&host=gridcrafthub&temp=venrolite
- http://www.ploughvale.org/
- http://www.townmarrow.org/
- http://www.projectkindlecoat.org/
here are some of the other chapters website (pretty bad!)
and here are some of the others:
- http://www.zrelkq.org/
- http://ovtu.org/
- http://www.lirvx.org/
Content Items that need to be included:
1. Logo
2. Menu - home, about, members, resources, events, membership, contact
3. Become a member - button or action
4. social links - friendwall, jobrungo, clipzora
5. banner - that needs to explain their purpose "Promoting environmental stewardship through operations, research, education and outreach" (or this can be worked into the design)
6. Upcoming event (s)
7. Advertisement - members can place an ad on the website, this can be a placeholder for now
8. newsletter signup
9. advertise with us - this link can be in the footer
30-60 years of age, succesfull (household budgets of 120K+ men and women that live in texas.
Education

```html
<!DOCTYPE html>
<html lang="en">
<head>
<meta charset="utf-8">
<title>Lone Star Wetland Flora Stewardship Guild</title>
<link rel="stylesheet" href="https://fonts.googleapis.com/css2?family=Cabin:wght@400;500&family=Open+Sans:wght@400;600&family=Arimo:wght@400&display=swap">
<style>
:root{
  --navy:#1d3f8f;
  --red:#d8394a;
  --red-dark:#b92535;
  --text:#555a60;
  --page:#ffffff;
  --footer-top:#4b4c50;
  --footer-bottom:#2e2f32;
  --footer-text:#f1f1f1;
  --blue-btn:#2f9be8;
  --dark-btn:#3b3c3f;
}
*{box-sizing:border-box;margin:0;padding:0}
html,body{width:1120px;height:1200px;overflow:hidden}
body{
  font-family:"Open Sans",sans-serif;
  background:linear-gradient(180deg,#5f86b0 0%,#a9c3dc 22%,#dfe9f0 36%,#8fa35a 48%,#6e8a4a 56%,#4d7395 64%,#6f8fb0 74%,#7a8a3e 86%,#4f6a2c 100%);
  position:relative;
}
.scenery{position:absolute;inset:0}
.page{
  position:absolute;left:113px;top:0;width:860px;height:1200px;
  background:var(--page);
}
/* header */
.brand{position:absolute;left:36px;top:58px;display:flex;align-items:center;gap:12px;width:300px}
.brand-mark{width:26px;height:26px;background:var(--red);flex:none}
.brand-name{font-family:"Cabin",sans-serif;font-weight:500;font-size:21px;line-height:1.2;color:var(--navy)}
.header-tools{position:absolute;right:37px;top:42px;display:flex;align-items:center;gap:8px}
.social-top{display:flex;gap:8px;margin-right:12px}
.social-top a{display:block;width:30px;height:30px;border:2px solid var(--navy);border-radius:50%}
.util-link{font-family:"Cabin",sans-serif;font-size:13px;color:#333;text-decoration:none;display:flex;align-items:center;gap:6px;padding:0 8px}
.util-link + .util-link{border-left:1px solid #ddd}
.btn-member{
  position:absolute;right:37px;top:99px;width:121px;height:32px;
  background:linear-gradient(#4a4b4e,#2f3033);color:#fff;border-radius:3px;
  font-family:"Cabin",sans-serif;font-size:12.5px;display:flex;align-items:center;justify-content:center;text-decoration:none
}
/* nav */
.main-nav{position:absolute;left:36px;top:183px;width:788px;height:38px;display:flex;background:linear-gradient(var(--red),#c72c3d)}
.main-nav a{
  font-family:"Cabin",sans-serif;font-size:13px;color:#fff;text-decoration:none;text-transform:uppercase;
  display:flex;align-items:center;justify-content:center;border-right:1px solid rgba(0,0,0,.15);box-shadow:inset -1px 0 rgba(255,255,255,.1)
}
.main-nav a.current{background:var(--red-dark)}
.main-nav a:last-child{border-right:none}
/* hero */
.hero{position:absolute;left:36px;top:221px;width:788px;height:437px;overflow:hidden}
.hero-photo{position:absolute;inset:0;background:linear-gradient(180deg,#f3f6ef 0%,#a7c56a 18%,#5f8a2e 38%,#6f8f78 55%,#3f5a2e 75%,#4d6a26 100%)}
.hero-arrow{position:absolute;top:170px;width:26px;height:26px}
.hero-arrow.prev{left:22px}.hero-arrow.next{right:22px}
.hero-caption{
  position:absolute;left:84px;top:253px;width:513px;height:86px;background:rgba(70,70,70,.72);
  padding:14px 0 0 6px;font-family:"Cabin",sans-serif;font-size:19px;line-height:31px;color:#fff;text-transform:uppercase
}
.hero-wave{position:absolute;left:0;bottom:0;width:788px;height:50px}
/* content */
.section-title{font-family:"Cabin",sans-serif;font-weight:400;font-size:20px;color:var(--navy);letter-spacing:-.2px}
.about{position:absolute;left:36px;top:694px;width:236px}
.about p{font-size:9.6px;line-height:17px;color:var(--text);margin-top:4px}
.about .section-title{margin-bottom:12px}
.events{position:absolute;left:324px;top:694px;width:240px}
.events .section-title{margin-bottom:20px}
.event{display:flex;gap:12px;margin-bottom:16px;height:50px}
.event-thumb{width:72px;height:52px;border:3px solid #fff;box-shadow:0 0 3px rgba(0,0,0,.3);flex:none}
.event-thumb.t1{background:linear-gradient(#9bbd7a,#3f6a4a)}
.event-thumb.t2{background:linear-gradient(#bcd6ec,#7a9a50 55%,#5d7e3e)}
.event-thumb.t3{background:linear-gradient(#b7d4ec,#6e9848 50%,#4f7040)}
.event h3{font-size:10px;font-weight:400;color:var(--red);margin-top:0}
.event p{font-size:8.6px;line-height:16px;color:var(--text);margin-top:2px}
.ad-slot{position:absolute;left:598px;top:699px;width:223px;height:223px;background:linear-gradient(180deg,#0c0c10 0%,#1b2a4a 40%,#0e0e12 72%,#d9d9d9 72%,#ececec 100%)}
/* footer */
.site-footer{position:absolute;left:0;top:970px;width:860px;height:180px;background:linear-gradient(var(--footer-top),var(--footer-bottom));color:var(--footer-text)}
.footer-col{position:absolute;top:30px}
.footer-col h4{font-family:"Arimo",sans-serif;font-weight:400;font-size:14px;margin-bottom:14px}
.footer-col li{list-style:none;font-size:9.6px;line-height:19.5px}
.col-advertise{left:36px}
.col-contact{left:227px}
.col-contact li{display:flex;gap:10px;align-items:flex-start}
.col-contact svg{flex:none;margin-top:4px}
.col-follow{left:429px;width:160px}
.col-follow p{font-size:9.6px;line-height:19.5px}
.social-foot{display:flex;gap:7px;margin-top:14px}
.social-foot span{width:20px;height:20px;border-radius:50%;background:#f4f4f4}
.col-news{left:637px;width:180px}
.col-news p{font-size:9.6px;line-height:19.5px}
.news-input{margin-top:8px;width:180px;height:23px;background:#fff;border:1px solid #ccc}
.news-btn{margin:11px 0 0 98px;width:81px;height:24px;background:var(--blue-btn);color:#fff;font-family:"Cabin",sans-serif;font-size:11.5px;display:flex;align-items:center;justify-content:center;text-transform:uppercase}
.copyright{position:absolute;left:0;top:1150px;width:860px;height:50px;background:#2c2d30;border-top:1px solid #3f4044;color:#f1f1f1;font-family:"Arimo",sans-serif;font-size:10px;padding:25px 0 0 36px}
</style>
</head>
<body>
<div class="scenery" role="img" aria-label="Wide river landscape with grassy banks under a blue sky with clouds"></div>

<div class="page">
  <header>
    <a class="brand" href="#"><span class="brand-mark"></span><span class="brand-name">Lone Star Wetland Flora Stewardship Guild</span></a>
    <div class="header-tools">
      <nav class="social-top">
        <a href="#" aria-label="friendwall"></a>
        <a href="#" aria-label="clipzora"></a>
        <a href="#" aria-label="jobrungo"></a>
      </nav>
      <a class="util-link" href="#"><svg width="9" height="11" viewBox="0 0 9 11"><rect x="0" y="5" width="9" height="6" fill="#444"/><path d="M2 5V3a2.5 2.5 0 0 1 5 0v2" fill="none" stroke="#444" stroke-width="1.4"/></svg>Login</a>
      <a class="util-link" href="#"><svg width="14" height="11" viewBox="0 0 14 11"><path d="M1 4l6-3 6 3v6H1z" fill="none" stroke="#444" stroke-width="1.3"/><path d="M1 4l6 4 6-4" fill="none" stroke="#444" stroke-width="1.3"/></svg>Contact</a>
    </div>
    <a class="btn-member" href="#">Become a Member</a>
  </header>

  <nav class="main-nav">
    <a class="current" href="#" style="width:81px">Home</a>
    <a href="#" style="width:122px">About Us</a>
    <a href="#" style="width:112px">Members</a>
    <a href="#" style="width:128px">Resources</a>
    <a href="#" style="width:103px">Events</a>
    <a href="#" style="width:129px">Membership</a>
    <a href="#" style="width:113px">Contact</a>
  </nav>

  <section class="hero">
    <div class="hero-photo" role="img" aria-label="Calm pond framed by tall reeds and green trees reflected in the water"></div>
    <svg class="hero-arrow prev" viewBox="0 0 26 26"><circle cx="13" cy="13" r="13" fill="rgba(0,0,0,.25)"/><path d="M15 8l-5 5 5 5" fill="none" stroke="#fff" stroke-width="1.4"/></svg>
    <svg class="hero-arrow next" viewBox="0 0 26 26"><circle cx="13" cy="13" r="13" fill="rgba(0,0,0,.25)"/><path d="M11 8l5 5-5 5" fill="none" stroke="#fff" stroke-width="1.4"/></svg>
    <div class="hero-caption">Promoting environmental stewardship through<br>operations, research, education and outreach</div>
    <svg class="hero-wave" viewBox="0 0 788 50" preserveAspectRatio="none"><path d="M0 44C150 58 280 40 420 20S680 -2 788 14V50H0z" fill="#fff"/></svg>
  </section>

  <section class="about">
    <h2 class="section-title">About Us</h2>
    <p>Claritas est etiam processus dynamicus, qui sequitur mutationem consuetudium lectorum. Mirum est notare quam littera gothica, quam nunc putamus parum claram, anteposuerit litterarum formas humanitatis per seacula quarta decima et quinta decima. Eodem modo typi, qui nunc nobis videntur parum clari, fiant sollemnes in futurum.</p>
    <p>Duis autem vel eum iriure dolor in hendrerit in vulputate velit esse molestie consequat, vel illum dolore eu feugiat nulla facilisis Claritas est etiam processus dynamicus, qui sequitur mutationem consuetudium lectorum. Mirum est notare quam littera gothica, quam nunc putamus.</p>
  </section>

  <section class="events">
    <h2 class="section-title">Upcoming Events</h2>
    <article class="event"><div class="event-thumb t1" role="img" aria-label="Pond covered with lily pads"></div><div><h3>Duis autem vel eum iriure dolor</h3><p>Brianne craves the endorphin rufu eled by fitness and uses it.</p></div></article>
    <article class="event"><div class="event-thumb t2" role="img" aria-label="Open marsh under a blue sky"></div><div><h3>Duis autem vel eum iriure dolor</h3><p>Brianne craves the endorphin rufu eled by fitness and uses it.</p></div></article>
    <article class="event"><div class="event-thumb t3" role="img" aria-label="Lake with floating water plants"></div><div><h3>Duis autem vel eum iriure dolor</h3><p>Brianne craves the endorphin rufu eled by fitness and uses it.</p></div></article>
  </section>

  <aside class="ad-slot" role="img" aria-label="Member advertisement: Clearbrook Agri Labs algae treatment jug and product label"></aside>

  <footer class="site-footer">
    <div class="footer-col col-advertise">
      <h4>Advertise with us</h4>
      <ul><li>Duis autem vel</li><li>Eodem modo typi</li><li>validations and verification</li><li>System monitoring</li><li>Emergency Breakdowns</li></ul>
    </div>
    <div class="footer-col col-contact">
      <h4>Contact Us</h4>
      <ul>
        <li><svg width="9" height="12" viewBox="0 0 9 12"><path d="M4.5 12S0 6.5 0 4.5a4.5 4.5 0 0 1 9 0C9 6.5 4.5 12 4.5 12z" fill="#bbb"/><circle cx="4.5" cy="4.5" r="1.6" fill="#444"/></svg><span>2450 Cypress Marsh Rd.<br>Caddo TX 75661</span></li>
        <li><svg width="12" height="9" viewBox="0 0 12 9"><rect width="12" height="9" fill="#bbb"/><path d="M0 0l6 5 6-5" fill="none" stroke="#444"/></svg><span>hello@lswfsg-mail.org</span></li>
        <li><svg width="10" height="10" viewBox="0 0 10 10"><path d="M2 0l2 3-1 1.5a6 6 0 0 0 2.5 2.5L7 6l3 2-1.5 2C4 10 0 6 0 1.5z" fill="#bbb"/></svg><span style="color:#bbb">55 412 0387</span></li>
      </ul>
    </div>
    <div class="footer-col col-follow">
      <h4>Follow Us</h4>
      <p>Follow us our news and events through social networks.</p>
      <div class="social-foot"><span aria-label="friendwall"></span><span aria-label="chirpline"></span><span aria-label="snapdotto"></span><span aria-label="reelvanta"></span></div>
    </div>
    <div class="footer-col col-news">
      <h4>Newsletter</h4>
      <p>Stay in touch with us by signing up for our quarterly newsletter!</p>
      <div class="news-input"></div>
      <div class="news-btn">Subscribe</div>
    </div>
  </footer>
  <div class="copyright">Copyright ©2013. All Rights Reserved.</div>
</div>
</body>
</html>
```